KWT Contracting services . Building and maintenance services, optic fibre installation

Business cards and logo design.I need a logo that I can use on business cards ,workwear and on my vehicles. I would like the KWT to be the main or larger text and contracting services to be the smaller or less important text.I like monograms, modern designs and repeating patterns symbols. I am also a Gemini and my favourite number is 22 so if this can be any inspiration to help with the design. Am thinking of the using German flag colours as a his is my family’s heritage. And the other 2 main colours I wear is black and white.But any ideas are appreciated.I do not need a design that is trade specific but a design that could be used for any business.

Target Market(s)

General public

Contact Information for Business Card

KWT Contracting Services ( front of business card)

(Back of business card)
Milo Brackwood
0471539264
Maintenance services
Optic fibre and data installation

Logo Text

Logo can just be pattern or monogram or incorporate KWT . I like the gemini star sign and the number 22

Colors
ec1f27
000000
fbee3e
ffffff

Requirements
Must have
• Logo and KWT Contracting Services on the front of business card
Nice to have
• Possible use of German flag colours.
• Modern design.
• Design to be able to be used on black or white background as I want to put it on clothing

```html
<!DOCTYPE html>
<html lang="en">
<head>
<meta charset="utf-8">
<title>KWT Contracting Services – Business Card</title>
<link href="https://fonts.googleapis.com/css2?family=Cinzel:wght@400;600&family=Exo+2:wght@400&display=swap" rel="stylesheet">
<style>
  :root {
    --page-bg: #ffffff;
    --card-dark: #050505;
    --card-mid: #1e1e1e;
    --gold: #d9b64a;
    --red: #ec1f27;
    --text-light: #e6e6e6;
    --text-soft: #c9c9c9;
    --rule: #bdbdbd;
  }
  * { box-sizing: border-box; margin: 0; padding: 0; }
  html, body { width: 1200px; height: 900px; overflow: hidden; background: var(--page-bg); }
  .stage {
    position: relative;
    width: 1200px;
    height: 900px;
    display: flex;
    align-items: center;
    justify-content: center;
    gap: 60px;
  }
  .card {
    position: relative;
    width: 520px;
    height: 310px;
    border-radius: 26px;
    overflow: hidden;
    background: var(--card-dark);
    box-shadow: 0 18px 30px rgba(0,0,0,0.18);
  }
  .card-pattern {
    position: absolute;
    inset: 0;
    background: radial-gradient(ellipse at 50% 48%, var(--card-mid) 0%, #101010 45%, var(--card-dark) 100%);
  }
  .card-content {
    position: relative;
    height: 100%;
    display: flex;
    flex-direction: column;
    align-items: center;
    justify-content: center;
    text-align: center;
  }
  .brand-mark {
    font-family: "Cinzel", serif;
    font-weight: 600;
    color: var(--gold);
    line-height: 1;
  }
  .card-front .brand-mark { font-size: 78px; letter-spacing: 2px; margin-bottom: 14px; }
  .company-name {
    font-family: "Cinzel", serif;
    font-weight: 400;
    color: var(--text-light);
    font-size: 21px;
    letter-spacing: 1px;
  }
  .company-tagline {
    display: flex;
    align-items: center;
    gap: 10px;
    margin-top: 2px;
    font-family: "Cinzel", serif;
    color: var(--text-light);
    font-size: 16px;
    letter-spacing: 1.5px;
  }
  .company-tagline::before,
  .company-tagline::after {
    content: "";
    width: 48px;
    height: 1px;
    background: var(--rule);
  }
  .card-back .brand-mark { font-size: 30px; margin-bottom: 18px; }
  .person-name {
    font-family: "Exo 2", sans-serif;
    color: var(--red);
    font-size: 17px;
    letter-spacing: 0.5px;
  }
  .person-phone {
    font-family: "Exo 2", sans-serif;
    color: var(--text-light);
    font-size: 18px;
    letter-spacing: 1.5px;
    margin-top: 8px;
  }
  .service-list {
    list-style: none;
    margin-top: 26px;
    font-family: "Exo 2", sans-serif;
    color: var(--text-soft);
    font-size: 14px;
    line-height: 1.5;
  }
</style>
</head>
<body>
  <main class="stage">
    <section class="card card-front">
      <div class="card-pattern" role="img" aria-label="Faint repeating monogram pattern on a black card background"></div>
      <div class="card-content">
        <div class="brand-mark">KWT</div>
        <div class="company-name">KWT Contracting</div>
        <div class="company-tagline">SERVICES</div>
      </div>
    </section>

    <section class="card card-back">
      <div class="card-pattern" role="img" aria-label="Faint repeating monogram pattern on a black card background"></div>
      <div class="card-content">
        <div class="brand-mark">KWT</div>
        <div class="person-name">Milo Brackwood</div>
        <div class="person-phone">0471539264</div>
        <ul class="service-list">
          <li>Maintenance services</li>
          <li>Optic fibre and data installation</li>
        </ul>
      </div>
    </section>
  </main>
</body>
</html>
```